Brindle Structures Construction Company Seeking Modern Website

We are a small construction company wanting to create a web presence. We don't have much in the way of current content but will get photos as they come in. Attached is a picture of our business card.
The pages we would like on the menu are:
Home
Portfolio
Product Specs
Testimonials
Our Process
Contact
Some designs we like are:
http://www.tovenquarnsheds.example/
http://www.qzrsheds.example/
http://pannowsheds.example/
http://wistenhalls.example/
Not much requirements other than that so feel free to be creative!
Updates
Target Market(s)
Construction
Commercial and Residential Buildings
Industry/Entity Type
Construction Company
Number of Pages Required
5+ page
Look and feel

```html
<!DOCTYPE html>
<html lang="en">
<head>
<meta charset="utf-8">
<title>Brindle Structures — Building dreams</title>
<link href="https://fonts.googleapis.com/css2?family=Lato:wght@300;400;700;900&display=swap" rel="stylesheet">
<style>
:root{
  --blue:#3a74ee;
  --blue-deep:#2f5fd8;
  --blue-light:#5a8ef5;
  --accent:#2a6de3;
  --title-soft:#9ab7f4;
  --pale:#eef5fd;
  --white:#ffffff;
  --text:#6b6f78;
  --red:#c4161c;
  --red-dark:#8e0f13;
  --ring:#d7e3f5;
  --client:#c9ced6;
}
*{margin:0;padding:0;box-sizing:border-box}
html,body{width:1200px;height:2429px;overflow:hidden}
body{font-family:"Lato",sans-serif;background:var(--white);position:relative;color:var(--text)}
.abs{position:absolute}
.center{left:0;width:1200px;text-align:center}

/* hero */
.hero{top:0;left:0;width:1200px;height:522px;overflow:hidden;
  background:linear-gradient(160deg,#4f86f3 0%,#3c74ea 50%,#3568e0 100%)}
.hero-photo{position:absolute;inset:0;
  background:linear-gradient(180deg,rgba(255,255,255,.06) 0%,rgba(30,60,160,.12) 60%,rgba(20,50,150,.18) 100%)}
.menu-toggle{top:60px;left:924px;width:18px}
.menu-toggle span{display:block;height:2px;background:var(--white);margin-bottom:4px}
.brand{top:124px;font-size:36px;font-weight:900;color:var(--white);letter-spacing:.5px}
.hero-title{top:230px;font-size:30px;font-weight:700;color:var(--white);line-height:38px;text-transform:uppercase;letter-spacing:.5px}
.hero-sub{top:322px;font-size:10.5px;color:#dfe8fd;line-height:20px;text-transform:uppercase;letter-spacing:.6px}
.btn{display:block;text-align:center;font-weight:900;text-transform:uppercase;border-radius:20px;font-size:9.5px;letter-spacing:.5px}
.btn-white{background:var(--white);color:var(--accent)}
.hero-btn{top:401px;left:538px;width:124px;height:34px;line-height:34px}
.scroll-arrow{top:487px;left:592px}

/* sections */
.section-title{font-size:30px;font-weight:300;color:var(--title-soft)}
.about{top:522px;left:0;width:1200px;height:243px;background:var(--white)}
.about .section-title{top:54px}
.about p{position:absolute;top:118px;left:270px;width:660px;text-align:center;font-size:10.5px;line-height:21px}

.expertise{top:765px;left:0;width:1200px;height:688px;background:var(--pale)}
.expertise .section-title{top:52px}
.service{position:absolute;width:230px;text-align:center}
.service-icon{width:84px;height:84px;margin:0 auto;border:1.5px solid var(--ring);border-radius:50%;display:flex;align-items:center;justify-content:center}
.service h3{margin-top:34px;font-size:15px;font-weight:900;color:var(--accent);letter-spacing:.3px}
.service p{margin-top:9px;font-size:10.5px;line-height:21px}

.works{top:1453px;left:0;width:1200px;height:610px;background:var(--white)}
.works .section-title{top:48px}
.work{position:absolute;width:215px;height:160px;border-radius:5px;box-shadow:0 2px 4px rgba(0,0,0,.25)}
.btn-red{background:var(--red);color:var(--white);border:1.5px solid var(--red-dark);box-shadow:0 2px 3px rgba(0,0,0,.2)}
.works-btn{top:537px;left:540px;width:120px;height:30px;line-height:28px}

.clients{top:2063px;left:0;width:1200px;height:219px;background:var(--pale)}
.clients .section-title{top:52px}
.client{position:absolute;top:126px;font-size:24px;font-weight:700;color:var(--client);text-align:center;width:160px}

.cta{top:2282px;left:0;width:1200px;height:147px;
  background:linear-gradient(120deg,#4a82f2 0%,#3a72ea 55%,#325fd6 100%)}
.cta-text{position:absolute;top:56px;left:257px;font-size:28px;font-weight:300;color:var(--white)}
.cta-text strong{font-weight:700}
.cta-btn{top:58px;left:819px;width:124px;height:34px;line-height:34px}
</style>
</head>
<body>

<header class="abs hero">
  <div class="hero-photo" role="img" aria-label="Photograph of a large two-storey family house under a blue tint"></div>
  <div class="abs menu-toggle"><span></span><span></span><span></span></div>
  <div class="abs center brand">Brindle Structures</div>
  <h1 class="abs center hero-title">Building dreams,<br>so you can build memories</h1>
  <p class="abs center hero-sub">Lorem ipsum dolor sit amet, consectetur adipisicing elit, sed do eiusmod tempor<br>incididunt ut labore et dolore magna aliqua. Ut enim ad minim veniam, quis nostrud</p>
  <a class="abs btn btn-white hero-btn">Hire us</a>
  <svg class="abs scroll-arrow" width="16" height="24" viewBox="0 0 16 24"><path d="M8 2v19M2 15l6 6 6-6" fill="none" stroke="#a9c3fa" stroke-width="1.4"/></svg>
</header>

<section class="abs about">
  <h2 class="abs center section-title">About Us</h2>
  <p>Lorem ipsum dolor sit amet, consectetur adipisicing elit, sed do eiusmod tempor incididunt ut labore et dolore magna aliqua. Ut enim ad minim veniam, quis nostrud exercitation ullamco laboris nisi ut aliquip ex ea commodo consequat. Duis aute irure dolor in reprehenderit in voluptate velit esse cillum dolore eu fugiat nulla pariatur. Excepteur sint occaecat cupidatat non proident, sunt in culpa qui officia</p>
</section>

<section class="abs expertise">
  <h2 class="abs center section-title">We Are Expert In</h2>

  <div class="service" style="left:251px;top:155px">
    <div class="service-icon"><svg width="40" height="36" viewBox="0 0 40 36"><path d="M20 3 2 19h5v15h10V24h6v10h10V19h5L31 10V4h-4v3z" fill="var(--accent)"/></svg></div>
    <h3>LOREM IPSUM</h3>
    <p>Lorem ipsum dolor sit amet, consectetur adipisicing elit, sed do eiusmod tempor incididunt ut labore et dolore magna aliqua. Ut enim ad minim</p>
  </div>
  <div class="service" style="left:486px;top:155px">
    <div class="service-icon"><svg width="36" height="40" viewBox="0 0 36 40"><path d="M8 4h4v24h-4z" fill="var(--accent)"/><path d="M4 28h12l-2 8H6z" fill="var(--accent)"/><rect x="20" y="26" width="12" height="10" rx="1" fill="var(--accent)"/></svg></div>
    <h3>LOREM IPSUM</h3>
    <p>Lorem ipsum dolor sit amet, consectetur adipisicing elit, sed do eiusmod tempor incididunt ut labore et dolore magna aliqua.</p>
  </div>
  <div class="service" style="left:719px;top:155px">
    <div class="service-icon"><svg width="40" height="36" viewBox="0 0 40 36"><path d="M14 8V4h12v4h-3V7h-6v1z" fill="var(--accent)"/><rect x="3" y="10" width="34" height="22" rx="2" fill="var(--accent)"/><rect x="3" y="17" width="34" height="2" fill="#eef5fd"/></svg></div>
    <h3>LOREM IPSUM</h3>
    <p>Lorem ipsum dolor sit amet, consectetur adipisicing elit, sed do eiusmod tempor incididunt ut labore et dolore magna aliqua. Ut enim ad minim</p>
  </div>

  <div class="service" style="left:251px;top:418px">
    <div class="service-icon"><svg width="40" height="30" viewBox="0 0 40 30"><path d="M6 22a14 14 0 0 1 28 0z" fill="var(--accent)"/><rect x="2" y="22" width="36" height="4" rx="2" fill="var(--accent)"/></svg></div>
    <h3>LOREM IPSUM</h3>
    <p>Lorem ipsum dolor sit amet, consectetur adipisicing elit, sed do eiusmod tempor incididunt ut labore et dolore magna aliqua. Ut enim ad minim</p>
  </div>
  <div class="service" style="left:486px;top:418px">
    <div class="service-icon"><svg width="40" height="30" viewBox="0 0 40 30"><path d="M4 14 26 6l10 6-22 9z" fill="var(--accent)"/><path d="M4 14v7l10 6v-6z" fill="#1f58c4"/><path d="M14 21v6l22-8v-7z" fill="#4a86f0"/></svg></div>
    <h3>LOREM IPSUM</h3>
    <p>Lorem ipsum dolor sit amet, consectetur adipisicing elit, sed do eiusmod tempor incididunt ut labore et dolore magna aliqua.</p>
  </div>
  <div class="service" style="left:719px;top:418px">
    <div class="service-icon"><svg width="36" height="40" viewBox="0 0 36 40"><path d="M18 2v20" stroke="var(--accent)" stroke-width="2"/><path d="M18 22a5 5 0 1 1-5 5" fill="none" stroke="var(--accent)" stroke-width="2.5"/><rect x="6" y="33" width="24" height="5" fill="var(--accent)"/></svg></div>
    <h3>LOREM IPSUM</h3>
    <p>Lorem ipsum dolor sit amet, consectetur adipisicing elit, sed do eiusmod tempor incididunt ut labore et dolore magna aliqua. Ut enim ad minim</p>
  </div>
</section>

<section class="abs works">
  <h2 class="abs center section-title">Latest Works</h2>
  <div class="work" style="left:259px;top:139px;background:linear-gradient(180deg,#8fb4dc 0%,#b8a27c 55%,#4f6b3a 100%)" role="img" aria-label="Photo of a finished stone-faced two-storey house"></div>
  <div class="work" style="left:494px;top:139px;background:linear-gradient(180deg,#c9d9ea 0%,#6a5a4e 55%,#3f6a32 100%)" role="img" aria-label="Photo of a dark painted Victorian-style house"></div>
  <div class="work" style="left:727px;top:139px;background:linear-gradient(180deg,#b9c9dc 0%,#9a4a36 55%,#5a6f48 100%)" role="img" aria-label="Photo of a red brick detached house"></div>
  <div class="work" style="left:259px;top:334px;background:linear-gradient(180deg,#4a88d8 0%,#e8dcc4 50%,#8a4a2c 100%)" role="img" aria-label="Photo of a white villa with terracotta roof"></div>
  <div class="work" style="left:494px;top:334px;background:linear-gradient(180deg,#d45b5a 0%,#e7a55a 50%,#4a4060 100%)" role="img" aria-label="Photo of a lit mansion with a pool at sunset"></div>
  <div class="work" style="left:727px;top:334px;background:linear-gradient(180deg,#8fb0d8 0%,#6d6a66 50%,#4f7a36 100%)" role="img" aria-label="Photo of a large suburban house with a lawn"></div>
  <a class="abs btn btn-red works-btn">All works</a>
</section>

<section class="abs clients">
  <h2 class="abs center section-title">Clients</h2>
  <div class="client" style="left:263px">Norvale</div>
  <div class="client" style="left:432px">Quenta</div>
  <div class="client" style="left:613px">Orvix</div>
  <div class="client" style="left:780px">Tamblo</div>
</section>

<section class="abs cta">
  <p class="cta-text">Need building works? <strong>Ready to work!</strong></p>
  <a class="abs btn btn-white cta-btn">Hire us</a>
</section>

</body>
</html>
```